Premium wine label refresh for Birch &Vale wines

Our Birch & Vale label is dated. We're looking for a contemporary refresh that will stand out on the shelf, make a strong quality statement and a more contemporary look. Feel free to take a completely fresh approach but the label should connect with the brand story. Birch & Vale refers to my convict ancestry and is a tribute to humble beginnings. Where we finish is not necessarily where we start.

Target Market(s)

Aspirational, educated wine drinkers 30-55

Industry/Entity Type

Wine

Font styles to use
Sans Serif

Requirements
Must have
• Shelf presence, premium feel, connection to the existing label
Nice to have
• Print quality cues like embossing, foil etc.
Should not have
• Fun look and feel.

```html
<!DOCTYPE html>
<html lang="en">
<head>
<meta charset="utf-8">
<title>Birch &amp; Vale — Hilltops Cabernet Sauvignon 2022</title>
<link rel="stylesheet" href="https://fonts.googleapis.com/css2?family=Tenor+Sans&family=Cutive&display=swap">
<style>
  :root {
    --page: #ffffff;
    --cream: #fbfbf0;
    --bronze: #a47c54;
    --bronze-light: #c9a070;
    --ink: #121118;
    --brand: #7a4e30;
    --line: #111111;
  }
  html, body {
    margin: 0;
    padding: 0;
    width: 1199px;
    height: 1200px;
    overflow: hidden;
    background: var(--page);
  }
  .canvas {
    position: relative;
    width: 1199px;
    height: 1200px;
  }
  .label {
    position: absolute;
    left: 225px;
    top: 294px;
    width: 747px;
    height: 611px;
    background: var(--cream);
    overflow: hidden;
  }
  .label-ground {
    position: absolute;
    inset: 0;
    width: 747px;
    height: 611px;
  }
  .brand-name {
    position: absolute;
    left: 0;
    right: 0;
    top: 57px;
    margin: 0;
    text-align: center;
    font-family: "Tenor Sans", sans-serif;
    font-weight: 400;
    font-size: 55px;
    letter-spacing: 4px;
    color: var(--brand);
    line-height: 1;
  }
  .emblem {
    position: absolute;
    left: 217px;
    top: 206px;
    width: 298px;
    height: 298px;
    border-radius: 50%;
    background: radial-gradient(circle at 50% 50%, #d8b27c 0 22%, #15141c 23% 62%, #c09466 63% 66%, #1c1b24 67% 100%);
  }
  .text {
    position: absolute;
    margin: 0;
    line-height: 1;
    color: var(--ink);
  }
  .region, .vintage {
    font-family: "Tenor Sans", sans-serif;
    font-size: 15px;
    letter-spacing: 1.5px;
    top: 524px;
  }
  .region { left: 68px; width: 104px; text-align: center; }
  .vintage { left: 588px; width: 90px; text-align: center; }
  .variety {
    font-family: "Cutive", serif;
    font-size: 22px;
    left: 183px;
    width: 381px;
    top: 553px;
    text-align: center;
  }
</style>
</head>
<body>
<div class="canvas">
  <div class="label">
    <svg class="label-ground" viewBox="0 0 747 611" aria-hidden="true">
      <path d="M0 222 H150 C210 222 240 200 262 182 C300 150 330 148 374 132 C418 148 448 150 486 182 C508 200 538 222 598 222 H747 V611 H0 Z" fill="var(--bronze)"/>
      <g fill="none" stroke="var(--line)" stroke-width="1.6">
        <polyline points="0,507 223,507 223,556 0,556"/>
        <polyline points="747,507 524,507 524,556 747,556"/>
        <rect x="183" y="538" width="381" height="50"/>
        <rect x="183" y="538" width="17" height="18"/>
        <rect x="206" y="538" width="17" height="18"/>
        <rect x="524" y="538" width="17" height="18"/>
        <rect x="547" y="538" width="17" height="18"/>
      </g>
    </svg>
    <h1 class="brand-name">BIRCH &amp; VALE</h1>
    <div class="emblem" role="img" aria-label="Art deco emblem with a gold padlock on a dark circular medallion"></div>
    <p class="text region">HILLTOPS</p>
    <p class="text vintage">2022</p>
    <p class="text variety">Cabernet Sauvignon</p>
  </div>
</div>
</body>
</html>
```